Title Insurance company and Construction Development company needs billboard design

Our Company Bramble Deed Partners and Bramble Buildworks based in the Chicago land area handles real estate closings and the development company does rehab work as well as new construction. We are looking for a billboard design that captures the attention of the people and excites them to use us. Would like to use the attached logo and we will probably add pictures of the leaders of both companies in the foreground. The size for the billboard is 14'x48'

Designs look the same

COVID

• Really want it to include our pics

```html
<!DOCTYPE html>
<html lang="en">
<head>
<meta charset="utf-8">
<title>Bramble Deed Partners &amp; Bramble Buildworks Billboard</title>
<link rel="stylesheet" href="https://fonts.googleapis.com/css2?family=Jost:ital,wght@0,500;0,600;0,700;0,800;1,400;1,800;1,900&display=swap">
<style>
  :root {
    --stage: #868686;
    --sky-top: #e9edf0;
    --sky-bottom: #f7f8f9;
    --ink: #24262b;
    --band-blue: #00b8f0;
    --band-red: #e03414;
    --white: #ffffff;
    --leader-tone-a: #2f4a6e;
    --leader-tone-b: #1e7fa8;
  }
  * { margin: 0; padding: 0; box-sizing: border-box; }
  html, body {
    width: 1200px; height: 1200px; overflow: hidden;
    background: var(--stage);
    font-family: "Jost", sans-serif;
  }
  .billboard {
    position: absolute; left: 50px; top: 440px;
    width: 1100px; height: 320px;
    background: var(--white); overflow: hidden;
  }
  .skyline {
    position: absolute; inset: 0 0 80px 0;
    background: linear-gradient(180deg, var(--sky-top) 0%, var(--sky-bottom) 55%, #dfe3e6 100%);
  }
  .brand {
    position: absolute; left: 26px; top: 60px; width: 160px;
    display: flex; flex-direction: column; align-items: center; gap: 8px;
    text-align: center;
  }
  .brand-dot { width: 56px; height: 56px; border-radius: 50%; background: var(--ink); }
  .brand-name {
    font-family: "Jost", sans-serif; font-weight: 700; font-size: 14px;
    line-height: 1.2; color: var(--ink);
  }
  .headline { position: absolute; left: 0; top: 0; color: var(--ink); }
  .headline span { position: absolute; white-space: nowrap; line-height: 1; }
  .line-title { left: 215px; top: 56px; font-size: 46px; font-style: italic; font-weight: 400; }
  .line-construction { left: 266px; top: 106px; font-size: 51px; font-style: italic; font-weight: 900; }
  .line-company { left: 194px; top: 159px; font-size: 41px; font-style: italic; font-weight: 800; }
  .leaders {
    position: absolute; left: 723px; top: 24px; width: 377px; height: 234px;
    background: linear-gradient(90deg, var(--leader-tone-a) 0%, var(--leader-tone-a) 50%, var(--leader-tone-b) 52%, var(--leader-tone-b) 100%);
    opacity: 0.85;
  }
  .contact-band {
    position: absolute; left: 0; bottom: 0; width: 730px; height: 80px;
    background: var(--band-blue);
  }
  .phone-icon { position: absolute; left: 80px; top: 20px; width: 46px; height: 46px; }
  .phone-divider { position: absolute; left: 147px; top: 24px; width: 3px; height: 40px; background: var(--white); }
  .phone-number {
    position: absolute; left: 172px; top: 6px;
    font-size: 68px; font-weight: 700; color: var(--white); letter-spacing: -1px; line-height: 1;
  }
  .names-band { position: absolute; right: 0; bottom: 0; width: 456px; height: 63px; }
  .names-band svg { position: absolute; inset: 0; }
  .names {
    position: absolute; inset: 0; display: flex; align-items: center;
    padding-left: 54px; color: var(--white); font-weight: 700; font-size: 17px; letter-spacing: 0.3px;
  }
  .names .slash { font-size: 32px; font-weight: 500; margin: 0 26px; }
</style>
</head>
<body>
  <main class="billboard">
    <div class="skyline" role="img" aria-label="Misty city skyline photograph behind the headline"></div>

    <div class="brand">
      <div class="brand-dot"></div>
      <p class="brand-name">Bramble Deed Partners<br>Bramble Buildworks</p>
    </div>

    <h1 class="headline">
      <span class="line-title">TITLE INSURANCE &amp;</span>
      <span class="line-construction">CONSTRUCTION</span>
      <span class="line-company">DEVELOPMENT COMPANY</span>
    </h1>

    <div class="leaders" role="img" aria-label="Portrait photograph of the two company leaders"></div>

    <div class="contact-band">
      <svg class="phone-icon" viewBox="0 0 46 46" aria-hidden="true">
        <path d="M9 6c2-2 4-2 5 0l5 8c1 2 0 3-1 4l-3 3c2 5 6 9 11 11l3-3c1-1 2-2 4-1l8 5c2 1 2 3 0 5l-4 4c-3 3-12 0-20-8S5 13 5 10z" fill="var(--white)"/>
        <path d="M26 6a14 14 0 0 1 14 14M26 13a7 7 0 0 1 7 7" stroke="var(--white)" stroke-width="3" fill="none" stroke-linecap="round"/>
      </svg>
      <div class="phone-divider"></div>
      <p class="phone-number">555.014.2290</p>
    </div>

    <div class="names-band">
      <svg viewBox="0 0 456 63" preserveAspectRatio="none" aria-hidden="true">
        <polygon points="51,0 456,0 456,63 0,63" fill="var(--band-red)"/>
      </svg>
      <p class="names">Rowan Hale<span class="slash">/</span>Lena Marsh</p>
    </div>
  </main>
</body>
</html>
```